vantro - business cards

Need business card designs - logo provided - see www.vantro.co.nz

Industry/Entity Type

Business

Requirements
Must have
• logo - provided in attachments
• www.vantro.co.nz

```html
<!DOCTYPE html>
<html lang="en">
<head>
<meta charset="utf-8">
<title>vantro – business cards</title>
<link rel="stylesheet" href="https://fonts.googleapis.com/css2?family=Cinzel:wght@400;600&display=swap">
<style>
  :root {
    --stage: #d9d9d9;
    --stage-edge: #bdbdbd;
    --charcoal: #3b3b3d;
    --charcoal-soft: #5a5a5c;
    --paper: #ffffff;
    --orange: #f07a2a;
    --orange-soft: #f6a36a;
    --ink-light: #f2f2f2;
    --ink-muted: #cfcfcf;
    --font-text: 'Cinzel', 'Times New Roman', serif;
  }
  * { box-sizing: border-box; margin: 0; padding: 0; }
  html, body { width: 1200px; height: 750px; overflow: hidden; }
  body {
    background: radial-gradient(ellipse at 45% 40%, #ececec 0%, var(--stage) 55%, var(--stage-edge) 100%);
    font-family: var(--font-text);
    position: relative;
  }
  .card {
    position: absolute;
    top: 232px;
    width: 500px;
    height: 286px;
    border-radius: 26px;
    overflow: hidden;
    background: var(--paper);
    box-shadow: 0 10px 24px rgba(0,0,0,0.22);
  }
  .card--front { left: 70px; }
  .card--back { left: 630px; }

  /* Front */
  .front-band { position: absolute; left: 0; width: 100%; overflow: hidden; }
  .front-band--top { top: 0; height: 84px; background: var(--charcoal); }
  .front-band--middle { top: 84px; height: 104px; background: var(--paper); }
  .front-band--bottom { top: 188px; height: 98px; background: var(--orange); }
  .band-watermark {
    position: absolute;
    left: 50%;
    top: 50%;
    transform: translate(-50%, -50%);
    font-family: var(--font-text);
    font-weight: 600;
    font-size: 58px;
    letter-spacing: 6px;
    line-height: 1;
    white-space: nowrap;
  }
  .front-band--top .band-watermark { color: rgba(255,255,255,0.06); }
  .front-band--bottom .band-watermark { color: rgba(255,255,255,0.14); }
  .brand {
    position: absolute;
    display: flex;
    align-items: center;
    gap: 12px;
    font-family: var(--font-text);
    font-weight: 600;
    color: var(--charcoal);
    line-height: 1;
    white-space: nowrap;
  }
  .brand__dot { border-radius: 50%; background: var(--orange); flex: none; }
  .front-band--middle .brand { left: 50%; top: 50%; transform: translate(-50%, -50%); font-size: 40px; }
  .front-band--middle .brand__dot { width: 30px; height: 30px; }

  /* Back */
  .back-art { position: absolute; inset: 0; }
  .card--back .brand { right: 28px; top: 22px; font-size: 20px; gap: 8px; }
  .card--back .brand__dot { width: 14px; height: 14px; }
  .holder { position: absolute; left: 70px; top: 92px; width: 230px; color: var(--ink-light); }
  .holder__name { font-size: 22px; font-weight: 400; letter-spacing: 1px; }
  .holder__title { font-size: 11px; color: var(--orange); text-align: right; letter-spacing: 1px; margin-top: 2px; }
  .holder__rule { height: 1px; background: var(--orange); margin: 8px 0 14px; }
  .contact { font-size: 8.5px; line-height: 1.45; color: var(--ink-muted); letter-spacing: 0.4px; }
  .company { margin-top: 16px; }
  .company__name { font-size: 11px; color: var(--orange); letter-spacing: 1px; }
</style>
</head>
<body>

<section class="card card--front" aria-label="Business card front">
  <div class="front-band front-band--top"><span class="band-watermark" aria-hidden="true">VANTRO</span></div>
  <div class="front-band front-band--middle">
    <div class="brand"><span class="brand__dot"></span><span class="brand__name">VANTRO</span></div>
  </div>
  <div class="front-band front-band--bottom"><span class="band-watermark" aria-hidden="true">VANTRO</span></div>
</section>

<section class="card card--back" aria-label="Business card back">
  <svg class="back-art" width="500" height="286" viewBox="0 0 500 286" aria-hidden="true">
    <circle cx="500" cy="300" r="92" fill="var(--orange-soft)"/>
    <circle cx="512" cy="310" r="90" fill="var(--orange)"/>
    <circle cx="196" cy="168" r="178" fill="var(--charcoal-soft)"/>
    <circle cx="188" cy="160" r="176" fill="var(--charcoal)"/>
  </svg>
  <div class="brand"><span class="brand__dot"></span><span class="brand__name">VANTRO</span></div>
  <div class="holder">
    <h1 class="holder__name">LIAM CARTER</h1>
    <p class="holder__title">TITLE HERE</p>
    <div class="holder__rule"></div>
    <p class="contact">PHONE : +64 00 000 00000<br>EMAIL : VANTRO@GMAIL.COM</p>
    <div class="company">
      <p class="company__name">"VANTRO"</p>
      <p class="contact">COMPANY PHONE NUMBER : 0800 VANTRO<br>(0800 826 876)<br>POSTAL ADDRESS (2 LINES, OR IN LINE)<br>WEB ADDRESS (WWW.VANTRO.CO.NZ)</p>
    </div>
  </div>
</section>

</body>
</html>
```